Lydia Vandermere personal business/name cards and stationery brief

I am looking for a simple design on my personal business cards, that I may use for all my stationery. All my stationery would be cream or ivory textured card, or cream/ivory quality paper. I am director of my family company and also property developer. But am wishing to have basic business cards that I can use across both businesses. I do not wish to have a title, just my initials as a focal point.
Target Market(s)
These are my personal business cards and stationery. I am looking for an elegant, relatively understated design that exudes wealth. There is no target audience, other than clients or people I already do business with. However design must be stylish and timeless.
If I am handing out my business card to anyone I do not do business with, or they are not contracting to me or my company currently, then i would like the target audience to wish they were.
I am 54 yeas of age, and my business cards must denote respect and class.
Industry/Entity Type
Business
Contact Information for Business Card
LV
Lydia Vandermere
Justice of the Peace
Possible rear of card
Mobile number
Email
Font styles to use
Requirements
Must have
- LV to be somehow entwined as a logo on the front of the card above my name
- These cards must state that I am a Justice of the Peace
- Colours only ivory or cream card with texture, and gold elegant font.
- Must be able to be used on all my stationery products
- Must be elegant, timeless and not cluttered
- Below are just some design I like. There is something in each design I like.
Nice to have
- I would like my initials to be the centre piece of the card. Somehow entwined together elegantly in a logo of sorts that I can use across all my stationery. But if not my initials, then something that is different and stands out from the rest.
Should not have
- Not gawdy or young. No colour. Nothing outlandish.

```html
<!DOCTYPE html>
<html lang="en">
<head>
<meta charset="utf-8">
<title>Lydia Vandermere — Business Card</title>
<link href="https://fonts.googleapis.com/css2?family=Questrial&display=swap" rel="stylesheet">
<style>
  :root {
    --backdrop-light: #f1efeb;
    --backdrop-dark: #c9c6c1;
    --card-cream: #e7dece;
    --card-cream-light: #efe7da;
    --card-cream-shade: #ddd2bf;
    --gold: #c88a4e;
    --gold-deep: #b8773c;
  }
  html, body {
    margin: 0;
    padding: 0;
    width: 1200px;
    height: 900px;
    overflow: hidden;
  }
  body {
    background: radial-gradient(ellipse at 50% 40%, var(--backdrop-light) 0%, #e4e1dc 60%, var(--backdrop-dark) 100%);
    font-family: "Questrial", "Helvetica Neue", Arial, sans-serif;
  }
  .card-stage {
    position: relative;
    width: 1200px;
    height: 900px;
    display: flex;
    align-items: center;
    justify-content: center;
    gap: 40px;
  }
  .business-card {
    width: 540px;
    height: 309px;
    background:
      radial-gradient(circle at 30% 25%, var(--card-cream-light) 0%, transparent 60%),
      linear-gradient(135deg, var(--card-cream) 0%, var(--card-cream-shade) 100%);
    box-shadow: 0 2px 3px rgba(0,0,0,0.25), 0 10px 24px rgba(0,0,0,0.12);
    display: flex;
    flex-direction: column;
    align-items: center;
    justify-content: center;
    color: var(--gold);
    text-align: center;
  }
  .card-back .holder-name {
    font-size: 30px;
    letter-spacing: 0.5px;
    margin: 0;
    line-height: 1.1;
    font-weight: 400;
  }
  .card-back .holder-title {
    font-size: 15px;
    margin: 4px 0 0;
    letter-spacing: 0.4px;
  }
  .card-back .divider {
    width: 18px;
    height: 1px;
    background: var(--gold);
    margin: 12px 0 10px;
  }
  .card-back .contact-line {
    font-size: 14px;
    margin: 2px 0;
    letter-spacing: 0.3px;
  }
  .card-front .monogram {
    font-size: 76px;
    letter-spacing: 4px;
    color: var(--gold-deep);
    line-height: 1;
    margin: 0;
    font-weight: 400;
  }
</style>
</head>
<body>
  <main class="card-stage">
    <section class="business-card card-back" aria-label="Card reverse">
      <h1 class="holder-name">Lydia Vandermere</h1>
      <p class="holder-title">Justice of the Peace</p>
      <div class="divider"></div>
      <p class="contact-line">+92 205 418 6630</p>
      <p class="contact-line">hello@lvmail.com</p>
    </section>
    <section class="business-card card-front" aria-label="Card front">
      <p class="monogram">LV</p>
    </section>
  </main>
</body>
</html>
```